International Life Insurer Needs a Web Design

What We Do: We are a boutique financial services firm specializing in solutions that financial services professionals can integrate into comprehensive wealth preservation strategies for their clients. Strategies we provide may run the spectrum from simple life insurance products to complex cases with very sophisticated and intricate solutions.

Industry Type: Financial & Insurance

Top Things to Communicate Through Our Web Design:
#1 Ultra High Net Worth
#2 INTERNATIONAL
#3 Private Banking
#4 Expertise
________________________________________
Our Target Audience:
Financial institutions/private banks who have high net worth/ultra high net worth international clients looking for unparalleled expertise in wealth preservation, taxation, and business insurance. The audience is the financial service professional, not the end client of the financial services. We will direct the professional to the site.
We Like These Designs. (fonts, colors, style):
Simple font, clean, modern, contemporary, blue colors
NOT stodgy, old, gothic, etc.

Secondarily, we’d like to also create a small tri-fold brochure incorporating the web elements (design, text), so the ability to transfer the design to print might be a plus.
Updates

Target Market(s)

Financial services professionals catering to their ultra high net worth clients

Industry/Entity Type

Life Insurance

Requirements
Must have
• Our logo (see uploaded file)
Nice to have
• the existing website includes some text that could be reviewed for ideas and incorporated into the design: http://harborlinecoveragepartners.example/

```html
<!DOCTYPE html>
<html lang="en">
<head>
<meta charset="utf-8">
<title>Harborline Coverage Partners</title>
<link rel="stylesheet" href="https://fonts.googleapis.com/css2?family=Montserrat:wght@400;500;600&family=Hind:wght@400;500;600&display=swap">
<style>
:root{
  --sky:#1a88da;
  --sky-deep:#0f6fc4;
  --topbar:#0b4a9a;
  --navy:#0d3d86;
  --navy-deep:#0a2f6c;
  --band:#1a5db3;
  --tweet:#17479a;
  --heading:#1a9ad6;
  --yellow:#ffe033;
  --red:#ee4a45;
  --text:#333;
  --grey:#6b6b6b;
  --line:#d4d4d4;
  --pale:#e6edf8;
}
*{box-sizing:border-box;margin:0;padding:0}
html,body{width:852px;height:1200px;overflow:hidden}
body{position:relative;background:#fff;font-family:"Hind",sans-serif;color:var(--text)}
.abs{position:absolute}
.hero-bg{left:0;top:0;width:852px;height:350px;background:linear-gradient(#1b8be0,#0f7ad0)}
.top-bar{left:0;top:0;width:852px;height:18px;background:var(--topbar)}
.top-social{top:3px;width:12px;height:12px;border-radius:50%;background:#dfe7f2}
.login{left:712px;top:3px;font-size:10px;color:#fff;display:flex;gap:4px;align-items:center}
.brand{left:100px;top:0;width:188px;height:74px;background:#fff;border-radius:0 0 6px 6px;box-shadow:0 2px 4px rgba(0,0,0,.25);display:flex;align-items:center;gap:8px;padding:0 12px}
.brand-mark{width:32px;height:32px;background:var(--sky-deep);flex:none}
.brand-name{font-family:"Montserrat",sans-serif;font-weight:500;font-size:13px;line-height:15px;color:var(--sky-deep)}
.call{left:594px;top:40px;color:#fff;display:flex;gap:8px}
.call-label{font-size:12px;font-weight:600;line-height:14px}
.call-number{font-family:"Montserrat",sans-serif;font-weight:600;font-size:17px;color:var(--yellow);letter-spacing:.5px}
.nav{left:100px;top:99px;width:652px;height:32px;background:linear-gradient(#fdfdfd,#d9d9d9);border-radius:4px;display:flex;align-items:stretch}
.nav-item{display:flex;align-items:center;justify-content:center;font-size:12px;color:#1f4f8f;border-right:1px solid #b9b9b9}
.search{left:566px;top:105px;width:169px;height:20px;background:#fff;border:1px solid #8aa8cf;border-radius:10px;font-size:10px;color:#777;font-family:Georgia,serif;padding:3px 8px}
.search-btn{left:710px;top:105px;width:25px;height:20px;background:var(--sky-deep);border-radius:0 10px 10px 0;display:flex;align-items:center;justify-content:center}
.slider{left:100px;top:145px;width:652px;height:253px;background:#f2f2f2;border-radius:4px;box-shadow:0 6px 10px rgba(0,0,0,.2)}
.slide{left:106px;top:151px;width:640px;height:240px;background:linear-gradient(100deg,#dfeaf3 0%,#c9d9e6 45%,#a7b7c4 70%,#39465a 100%)}
.arrow{top:258px;width:16px;height:28px;background:#e9e9e9;display:flex;align-items:center;justify-content:center}
.dots{left:384px;top:380px;width:60px;height:14px;background:#eee;border-radius:6px 6px 0 0;display:flex;gap:3px;justify-content:center;align-items:center}
.dot{width:6px;height:6px;border-radius:50%;background:#8a8a8a}
.h2{font-family:"Montserrat",sans-serif;font-weight:500;color:var(--heading);font-size:22px}
.about p{font-size:11px;line-height:16px;width:420px;margin-bottom:16px}
.read-more{font-size:11px;color:var(--red)}
.contact{left:550px;top:442px;width:202px;height:183px;border:2px solid var(--sky-deep);border-radius:4px;background:var(--pale);overflow:hidden}
.contact-head{height:30px;background:#1e5fb5;color:var(--yellow);font-family:"Montserrat",sans-serif;font-weight:500;font-size:17px;padding:4px 16px}
.field{left:17px;width:164px;height:19px;background:linear-gradient(#f4f4f4,#d4d4d4);border:1px solid #a8a8a8;font-size:10px;padding:3px 5px;color:#333}
.btn{background:var(--red);color:#fff;border-radius:3px;display:flex;align-items:center;justify-content:center}
.rule{left:100px;top:651px;width:652px;height:1px;background:var(--line)}
.service-img{top:710px;width:199px;height:69px;border:1px solid #bbb}
.service-title{top:786px;font-family:"Montserrat",sans-serif;font-weight:500;font-size:17px;color:#222}
.service-text{top:810px;width:200px;font-size:11px;line-height:16px}
.service-btn{top:851px;width:61px;height:13px;font-size:7px;font-weight:600}
.newsletter{left:100px;top:908px;width:652px;height:44px;border:1px solid #aaa;border-radius:3px;background:linear-gradient(#fafafa,#dedede)}
.news-title{left:78px;top:4px;font-size:15px;font-weight:600;color:#666}
.news-sub{left:78px;top:24px;font-size:9px;color:#888}
.news-input{left:336px;top:9px;width:207px;height:23px;background:#fff;border:1px solid #bbb;font-family:Georgia,serif;font-size:10px;color:#555;padding:5px 6px}
.divider{left:0;top:966px;width:852px;height:14px;background:linear-gradient(#f4f4f4,#c8c8c8)}
.testimonial-band{left:0;top:980px;width:852px;height:75px;background:var(--band)}
.yellow-head{font-size:12px;font-weight:600;color:var(--yellow)}
.tweet{left:338px;top:993px;width:414px;height:51px;background:var(--tweet);border:1px solid #2b63b8;border-radius:3px}
.footer{left:0;top:1055px;width:852px;height:125px;background:var(--navy)}
.foot-line{height:1px;background:#2e5ba0}
.foot-label{font-size:9px;color:#6fb2ee}
.foot-text{font-size:10px;color:#fff}
.social{top:1130px;width:29px;height:29px;border-radius:50%;background:linear-gradient(#fafafa,#bcbcbc)}
.bottom-bar{left:0;top:1180px;width:852px;height:20px;background:var(--navy-deep);font-size:9px;color:#fff}
</style>
</head>
<body>
<div class="abs hero-bg"></div>
<div class="abs top-bar"></div>
<div class="abs top-social" style="left:647px"></div>
<div class="abs top-social" style="left:665px"></div>
<div class="abs top-social" style="left:684px"></div>
<div class="abs login">Log In
  <svg width="10" height="11" viewBox="0 0 10 11"><rect x="1" y="5" width="8" height="6" fill="#ffd23a"/><path d="M3 5V3a2 2 0 0 1 4 0v2" stroke="#ffd23a" stroke-width="1.5" fill="none"/></svg>
</div>

<header class="abs brand">
  <div class="brand-mark"></div>
  <div class="brand-name">Harborline Coverage Partners</div>
</header>

<div class="abs call">
  <svg width="26" height="26" viewBox="0 0 24 24"><path d="M6.6 10.8a15.1 15.1 0 0 0 6.6 6.6l2.2-2.2c.3-.3.7-.4 1-.2 1.1.4 2.3.6 3.6.6.6 0 1 .4 1 1V20c0 .6-.4 1-1 1A17 17 0 0 1 3 4c0-.6.4-1 1-1h3.5c.6 0 1 .4 1 1 0 1.3.2 2.5.6 3.6.1.3 0 .7-.2 1z" fill="var(--yellow)"/></svg>
  <div><div class="call-label">Call Us Now!</div><div class="call-number">0100 555 0199</div></div>
</div>

<nav class="abs nav">
  <div class="nav-item" style="width:49px">
    <svg width="14" height="13" viewBox="0 0 14 13"><path d="M7 0 0 6h2v7h4V9h2v4h4V6h2z" fill="#1f4f8f"/></svg>
  </div>
  <div class="nav-item" style="width:79px">About Us</div>
  <div class="nav-item" style="width:70px">Services</div>
  <div class="nav-item" style="width:94px">Case Studies</div>
  <div class="nav-item" style="width:84px">Contact Us</div>
</nav>
<div class="abs search">Search:</div>
<div class="abs search-btn"><svg width="10" height="10" viewBox="0 0 10 10"><circle cx="4" cy="4" r="3" stroke="#fff" stroke-width="1.5" fill="none"/><path d="M6 6l3 3" stroke="#fff" stroke-width="1.5"/></svg></div>

<div class="abs slider"></div>
<div class="abs slide" role="img" aria-label="Advisers meeting with a client at a desk in a bright modern office"></div>
<div class="abs arrow" style="left:106px;border-radius:0 14px 14px 0"><svg width="8" height="12" viewBox="0 0 8 12"><path d="M6 1 1 6l5 5" stroke="#444" stroke-width="2" fill="none"/></svg></div>
<div class="abs arrow" style="left:730px;border-radius:14px 0 0 14px"><svg width="8" height="12" viewBox="0 0 8 12"><path d="M2 1l5 5-5 5" stroke="#444" stroke-width="2" fill="none"/></svg></div>
<div class="abs dots"><span class="dot"></span><span class="dot" style="background:#1e5fb5"></span><span class="dot"></span><span class="dot"></span></div>

<section class="abs about" style="left:100px;top:437px">
  <h2 class="h2" style="margin-bottom:8px">What We Do?</h2>
  <p>We are a boutique financial services firm specializing in solutions that financial services professionals can integrate into comprehensive wealth preservation strategies for their clients. Strategies we provide may run the spectrum from simple life insurance products to complex cases with very sophisticated and intricate solutions.</p>
  <p>Financial services professionals can integrate into comprehensive wealth preservation strategies for their clients. Strategies we provide may run the spectrum from simple life insurance products.</p>
  <div class="read-more">Read More &rarr;</div>
</section>

<aside class="abs contact">
  <div class="contact-head">Contact Us</div>
  <div class="abs field" style="top:38px">Name:</div>
  <div class="abs field" style="top:64px">Email:</div>
  <div class="abs field" style="top:90px;height:47px">Massage:</div>
  <div class="abs btn" style="left:17px;top:144px;width:88px;height:23px;font-size:13px">SEND NOW</div>
</aside>

<div class="abs rule"></div>

<h2 class="abs h2" style="left:100px;top:673px">Our Services</h2>
<div class="abs service-img" style="left:100px;background:linear-gradient(#4d9a3c,#2f6f29)" role="img" aria-label="Hand sketching success words on a green chalkboard"></div>
<div class="abs service-img" style="left:326px;background:linear-gradient(#1f5aa0,#0a2452)" role="img" aria-label="Glowing world map with connection lines"></div>
<div class="abs service-img" style="left:552px;background:linear-gradient(90deg,#0b2d6e,#c89032 50%,#0b2d6e)" role="img" aria-label="Golden padlocks on a digital blue background"></div>

<div class="abs service-title" style="left:100px">Ultra High Net Worth</div>
<div class="abs service-title" style="left:326px">International</div>
<div class="abs service-title" style="left:552px">Private Banking</div>
<p class="abs service-text" style="left:100px">Lorem Ipsum is simply dummy content text of the typesetting industry.</p>
<p class="abs service-text" style="left:326px">Lorem Ipsum is simply dummy content text of the typesetting industry.</p>
<p class="abs service-text" style="left:552px">Lorem Ipsum is simply dummy content text of the typesetting industry.</p>
<div class="abs btn service-btn" style="left:100px">READ MORE</div>
<div class="abs btn service-btn" style="left:326px">READ MORE</div>
<div class="abs btn service-btn" style="left:552px">READ MORE</div>

<div class="abs newsletter">
  <svg class="abs" style="left:14px;top:-6px" width="58" height="42" viewBox="0 0 58 42"><g transform="rotate(-15 29 21)"><rect x="6" y="8" width="46" height="28" fill="#fbd468" stroke="#c99a2a"/><path d="M6 8l23 16 23-16" stroke="#c99a2a" fill="none"/></g></svg>
  <div class="abs news-title">Get Newsletter!</div>
  <div class="abs news-sub">Lorem Ipsum is simply dummy text of the typesetting industry.</div>
  <div class="abs news-input">Enter your email:</div>
  <div class="abs btn" style="left:550px;top:9px;width:88px;height:24px;font-size:13px">SUBMIT</div>
</div>

<div class="abs divider"></div>
<div class="abs testimonial-band"></div>
<div class="abs yellow-head" style="left:100px;top:985px;font-size:13px">Testimonial</div>
<p class="abs foot-text" style="left:100px;top:1009px;width:210px;font-size:9px;line-height:15px">Lorem Ipsum is simply dummy text of the typesetting industry.</p>
<div class="abs tweet">
  <div class="abs" style="left:20px;top:12px;width:26px;height:26px;border-radius:50%;background:#4aa8ee"></div>
  <p class="abs foot-text" style="left:75px;top:12px;font-size:9px">Lorem Ipsum is simply dummy <span style="color:#7fc6ff;font-size:11px">harborline.example/news</span> industry.</p>
  <p class="abs" style="left:75px;top:30px;font-size:7px;color:#b9cbe8">10 days ago</p>
</div>

<footer class="abs footer">
  <div class="abs yellow-head" style="left:100px;top:16px">Cotact Us</div>
  <div class="abs foot-line" style="left:100px;top:40px;width:263px"></div>
  <div class="abs foot-label" style="left:100px;top:50px">Address:</div>
  <div class="abs foot-text" style="left:100px;top:63px;font-size:9px">502, Lorem Ipsum is simply text printing, typesetting 012345</div>
  <div class="abs foot-label" style="left:100px;top:82px">Phone: <span style="color:#fff;font-size:15px">0100 555 0199</span></div>
  <div class="abs foot-label" style="left:100px;top:103px">Email: <span style="color:#fff;text-decoration:underline">info@harborline.example</span></div>
  <div class="abs yellow-head" style="left:472px;top:16px">Stay In Touch</div>
  <div class="abs foot-line" style="left:472px;top:40px;width:264px"></div>
  <div class="abs foot-label" style="left:473px;top:50px">Visit My Social Media:</div>
</footer>
<div class="abs social" style="left:473px"></div>
<div class="abs social" style="left:509px"></div>
<div class="abs social" style="left:545px"></div>

<div class="abs bottom-bar">
  <span class="abs" style="left:100px;top:5px">© 2012 Harborline Coverage Partners | All Right Reserved</span>
  <span class="abs" style="left:529px;top:5px">Home &nbsp;| &nbsp;About Us &nbsp;| &nbsp;Services &nbsp;| &nbsp;Case Study &nbsp;| &nbsp;Contact Us</span>
</div>
</body>
</html>
```